Birchwood Clover Business Cards

I need a business card with my logo, number, Facebook account, and some information about what I am selling. Green card with logo on the front. 555-218-3946 phone number, @birchwoodclover Facebook, •Orchardgrass Hay •Alfalfa Hay •Mixed Grass Hay , and “Premium Quality Hay” all written on the back.

Target Market(s)

Hay

Contact Information for Business Card

Phone number, Facebook, different types of hay.

Colors
00AB8E
00BBA5
67D7C9
C6EFE9
E9F9F6

```html
<!DOCTYPE html>
<html lang="en">
<head>
<meta charset="utf-8">
<title>Birchwood Clover Business Cards</title>
<link rel="stylesheet" href="https://fonts.googleapis.com/css2?family=Poppins:wght@400;500;600&family=Kaushan+Script&display=swap">
<style>
  :root {
    --stage: #e4e4e4;
    --field-green: #00a651;
    --deep-green: #00a651;
    --mint: #cdebe6;
    --ink: #1a1a1a;
    --white: #ffffff;
  }
  * { box-sizing: border-box; margin: 0; padding: 0; }
  html, body { width: 1200px; height: 852px; overflow: hidden; }
  body {
    background: var(--stage);
    font-family: "Poppins", sans-serif;
    position: relative;
  }
  .card {
    position: absolute;
    width: 540px;
    height: 310px;
    border-radius: 22px;
    overflow: hidden;
    box-shadow: 0 10px 24px rgba(0,0,0,0.18);
  }

  /* Front */
  .card-front {
    left: 50px; top: 110px;
    background: var(--field-green);
  }
  .brand-mark {
    position: absolute;
    left: 95px; top: 88px;
    display: flex; align-items: center; gap: 18px;
  }
  .brand-mark__dot {
    width: 64px; height: 64px; border-radius: 50%;
    background: var(--white);
    flex: none;
  }
  .brand-mark__text { display: flex; flex-direction: column; }
  .brand-mark__name {
    font-weight: 600; font-size: 30px; line-height: 1.1;
    color: var(--ink);
  }
  .brand-mark__phone {
    font-weight: 600; font-size: 34px; line-height: 1.2;
    color: var(--ink); letter-spacing: 0.5px;
  }
  .front-tagline {
    position: absolute;
    left: 0; right: 0; top: 218px;
    text-align: center;
    font-family: "Kaushan Script", cursive;
    font-size: 24px;
    color: var(--ink);
  }

  /* Back */
  .card-back {
    left: 610px; top: 430px;
    background: var(--mint);
  }
  .back-wave { position: absolute; inset: 0; }
  .back-brand {
    position: absolute;
    right: 36px; top: 34px;
    display: flex; align-items: center; gap: 10px;
  }
  .back-brand__dot {
    width: 34px; height: 34px; border-radius: 50%;
    background: var(--deep-green);
  }
  .back-brand__name {
    font-weight: 600; font-size: 17px; color: var(--deep-green);
  }
  .contact {
    position: absolute;
    left: 42px; top: 112px;
  }
  .contact__name { font-weight: 500; font-size: 22px; color: var(--ink); line-height: 1.2; }
  .contact__role { font-weight: 500; font-size: 15px; color: var(--deep-green); margin-bottom: 10px; }
  .contact__line {
    display: flex; align-items: center; gap: 10px;
    font-size: 15px; color: var(--ink);
    margin: 0 0 6px 18px;
  }
  .contact__icon {
    width: 18px; height: 18px; border-radius: 50%;
    background: var(--deep-green);
    display: flex; align-items: center; justify-content: center;
    flex: none;
  }
  .hay-list {
    position: absolute;
    right: 24px; bottom: 20px;
    display: flex; gap: 16px;
    list-style: none;
    color: var(--white);
    font-size: 13px;
  }
  .hay-list li { display: flex; align-items: center; gap: 6px; }
</style>
</head>
<body>

<section class="card card-front" aria-label="Card front">
  <div class="brand-mark">
    <span class="brand-mark__dot"></span>
    <div class="brand-mark__text">
      <span class="brand-mark__name">Birchwood Clover</span>
      <span class="brand-mark__phone">555-218-3946</span>
    </div>
  </div>
  <p class="front-tagline">Premium Quality Hay</p>
</section>

<section class="card card-back" aria-label="Card back">
  <svg class="back-wave" viewBox="0 0 540 310" preserveAspectRatio="none" aria-hidden="true">
    <path d="M0,262 C110,250 200,262 300,222 C390,186 460,168 540,182 L540,310 L0,310 Z" fill="var(--deep-green)"/>
  </svg>

  <div class="back-brand">
    <span class="back-brand__dot"></span>
    <span class="back-brand__name">Birchwood Clover</span>
  </div>

  <div class="contact">
    <p class="contact__name">Daniel Reyes</p>
    <p class="contact__role">Owner</p>
    <p class="contact__line">
      <span class="contact__icon">
        <svg width="10" height="10" viewBox="0 0 24 24" aria-hidden="true"><path fill="#fff" d="M6.6 10.8a15 15 0 0 0 6.6 6.6l2.2-2.2a1 1 0 0 1 1-.25 11.4 11.4 0 0 0 3.6.6 1 1 0 0 1 1 1V20a1 1 0 0 1-1 1A17 17 0 0 1 3 4a1 1 0 0 1 1-1h3.5a1 1 0 0 1 1 1c0 1.25.2 2.45.6 3.6a1 1 0 0 1-.25 1z"/></svg>
      </span>
      555-218-3946
    </p>
    <p class="contact__line">
      <span class="contact__icon"></span>
      @birchwoodclover
    </p>
  </div>

  <ul class="hay-list">
    <li><svg width="12" height="10" viewBox="0 0 12 10" aria-hidden="true"><path d="M6 10V5M6 5C4 2 1 3 0 4c2 2 4 2 6 1zm0 0c2-3 5-2 6-1-2 2-4 2-6 1z" fill="#fff" stroke="#fff" stroke-width="0.8"/></svg>Orchardgrass Hay</li>
    <li><svg width="12" height="10" viewBox="0 0 12 10" aria-hidden="true"><path d="M6 10V5M6 5C4 2 1 3 0 4c2 2 4 2 6 1zm0 0c2-3 5-2 6-1-2 2-4 2-6 1z" fill="#fff" stroke="#fff" stroke-width="0.8"/></svg>Alfalfa Hay</li>
    <li><svg width="12" height="10" viewBox="0 0 12 10" aria-hidden="true"><path d="M6 10V5M6 5C4 2 1 3 0 4c2 2 4 2 6 1zm0 0c2-3 5-2 6-1-2 2-4 2-6 1z" fill="#fff" stroke="#fff" stroke-width="0.8"/></svg>Mixed Grass Hay</li>
  </ul>
</section>

</body>
</html>
```